Business Card Design

Cake decorating business in a small town in Australia. looking for a style that is fresh with a touch of vintage/country. liking these ideas, timber backgrounds, chalkboards, bunting, flowers and cake elements (rolling pins, cupcakes, cake stands, etc.) would consider a shot saying/statement. would like the back of the card to have wording "Specialising in delectable treats for all your special occasions" - wedding cakes - birthday cakes - special occasion cakes - novelty cakes - cupcakes, cookies, slices and cake pops. maybe incorporate a cake in design on back page. attached are a few of my favourite cakes and the start of a card design I liked.

Industry/Entity Type

Business

Contact Information for Business Card

Marigold's Sugarloft Bakes 0438 056 969Find me on (Chirpwall Logo)

Requirements
Nice to have
• timber, some of my designs, chalkboard, baking utensils
Should not have
• no red font

```html
<!DOCTYPE html>
<html lang="en">
<head>
<meta charset="utf-8">
<title>Marigold's Sugarloft Bakes – Business Card</title>
<link rel="stylesheet" href="https://fonts.googleapis.com/css2?family=Tinos:wght@400;700&display=swap">
<style>
  :root {
    --backdrop: #6b5139;
    --magenta: #a3197f;
    --magenta-deep: #8a136b;
    --timber-light: #c9c9c9;
    --timber-dark: #8c8c8c;
    --plum: #8d3f8a;
    --plum-deep: #6e2a6b;
    --band: #2e0b28;
    --ink: #111111;
    --white: #ffffff;
    --tan: #e8b98c;
    --chip: #3b5998;
  }
  * { margin: 0; padding: 0; box-sizing: border-box; }
  html, body { width: 1000px; height: 1200px; overflow: hidden; }
  body {
    background: var(--backdrop);
    font-family: "Tinos", "Times New Roman", serif;
    position: relative;
  }
  .card {
    position: absolute;
    left: 75px;
    width: 857px;
    border-radius: 22px;
    overflow: hidden;
    box-shadow: 0 6px 18px rgba(0,0,0,.45);
  }
  /* Front */
  .card-front { top: 57px; height: 520px; }
  .card-front .timber {
    position: absolute; inset: 0;
    background: linear-gradient(90deg, var(--timber-dark), var(--timber-light) 30%, #a9a9a9 60%, var(--timber-light) 85%, var(--timber-dark));
  }
  .card-front .wave { position: absolute; inset: 0; }
  .holder-name {
    position: absolute; left: 45px; top: 45px;
    color: var(--white); font-size: 33px; line-height: 1;
  }
  .holder-title {
    position: absolute; left: 45px; top: 87px;
    color: var(--white); font-size: 23px;
  }
  .brand-name {
    position: absolute; left: 380px; top: 150px; width: 440px;
    text-align: center; color: var(--white);
    font-size: 34px; line-height: 1.25;
  }
  .contact {
    position: absolute; left: 43px; top: 428px;
    color: var(--ink); font-size: 21px; line-height: 30px;
  }
  .social {
    position: absolute; left: 574px; top: 470px;
    display: flex; align-items: center; gap: 12px;
    color: var(--ink); font-size: 19px;
  }
  .social .chip { width: 22px; height: 22px; background: var(--chip); }
  /* Back */
  .card-back {
    top: 620px; height: 530px;
    background: radial-gradient(ellipse at 50% 40%, var(--plum), var(--plum-deep));
  }
  .gallery {
    position: absolute; top: 42px; left: 30px;
    display: flex; gap: 22px;
  }
  .gallery-photo {
    width: 251px; height: 288px;
    border: 2px solid #4a3a44;
  }
  .photo-travel { background: linear-gradient(180deg, #8a7a62, #d49a4a 55%, #7a2a1e); }
  .photo-boots { background: linear-gradient(160deg, #e6e4df, #8b5a36 45%, #c9a870); }
  .photo-tiers { background: linear-gradient(180deg, #7a6552, #4a8fd0 45%, #8cc63e 75%, #6d5a48); }
  .tagline-band {
    position: absolute; left: 0; right: 0; bottom: 0; height: 143px;
    background: var(--band);
    text-align: center; padding-top: 22px;
  }
  .tagline {
    color: var(--white); font-weight: 700; font-size: 24px;
  }
  .services {
    margin-top: 10px; color: var(--tan); font-size: 19px; line-height: 24px;
  }
</style>
</head>
<body>
  <section class="card card-front">
    <div class="timber" role="img" aria-label="Grey weathered timber planks"></div>
    <svg class="wave" width="857" height="520" viewBox="0 0 857 520">
      <defs>
        <filter id="wave-shadow" x="-5%" y="-5%" width="110%" height="120%">
          <feDropShadow dx="0" dy="4" stdDeviation="4" flood-color="#000" flood-opacity=".45"/>
        </filter>
      </defs>
      <path filter="url(#wave-shadow)" fill="var(--magenta)"
        d="M0 0 H857 V410 C820 440 740 440 640 395 C520 335 440 255 320 205 C220 165 100 160 0 180 Z"/>
    </svg>
    <div class="holder-name">Your name here</div>
    <div class="holder-title">Title here</div>
    <div class="brand-name">Marigold's Sugarloft Bakes</div>
    <div class="contact">
      <div>Phone: 0417 382 254</div>
      <div>Email: hello@sugarloftbakes.example</div>
    </div>
    <div class="social">Find me on Chirpwall <span class="chip"></span></div>
  </section>

  <section class="card card-back">
    <div class="gallery">
      <div class="gallery-photo photo-travel" role="img" aria-label="Photo of a stacked suitcase cake topped with a globe for a 21st birthday"></div>
      <div class="gallery-photo photo-boots" role="img" aria-label="Photo of a boots and cowboy hat novelty cake on a timber board for a 50th birthday"></div>
      <div class="gallery-photo photo-tiers" role="img" aria-label="Photo of a two-tier blue and green first birthday cake with a number one topper"></div>
    </div>
    <div class="tagline-band">
      <p class="tagline">Specialising in delectable treats for all your special occasions</p>
      <p class="services">wedding cakes|birthday cakes|special occasion cakes novelty cakes<br>cupcakes|cookies,slices and cake pops.</p>
    </div>
  </section>
</body>
</html>
```